Rollers & Glides.com

Vertical Business Card with focus on branding with our icon. Information on card will be logo, persons name, position, phone number, email address and website. Use the the name Marcus Tilden, position President, phone number 555.214.8890, email Marcus@rollersandglides.com, website www.rollersandglides.com.

```html
<!DOCTYPE html>
<html lang="en">
<head>
<meta charset="utf-8">
<title>Rollers &amp; Glides.com — Business Card</title>
<link rel="stylesheet" href="https://fonts.googleapis.com/css2?family=Arimo:wght@400;700&family=Roboto+Condensed:wght@400&display=swap">
<style>
  :root {
    --backdrop: #d3d0ca;
    --brand-blue: #1a45a0;
    --silver: #c3c7cf;
    --card-white: #fbfbfa;
    --ink: #3a3a3a;
    --ink-soft: #555555;
  }
  * { margin: 0; padding: 0; box-sizing: border-box; }
  html, body { width: 1200px; height: 837px; overflow: hidden; }
  body {
    background: var(--backdrop);
    position: relative;
    font-family: "Arimo", Arial, sans-serif;
  }
  .card {
    position: absolute;
    top: 150px;
    width: 300px;
    height: 525px;
    border-radius: 3px;
    box-shadow: 0 6px 18px rgba(0,0,0,0.12);
    display: flex;
    flex-direction: column;
    align-items: center;
  }
  .card--back {
    left: 260px;
    background: var(--brand-blue);
    justify-content: center;
    gap: 22px;
  }
  .brand-dot {
    width: 56px;
    height: 56px;
    border-radius: 50%;
    background: var(--silver);
  }
  .brand-name--back {
    font-family: "Roboto Condensed", "Arial Narrow", sans-serif;
    font-size: 28px;
    letter-spacing: 1px;
    color: var(--silver);
    white-space: nowrap;
  }
  .card--front {
    left: 640px;
    background: var(--card-white);
    padding: 90px 0 0;
  }
  .front-brand {
    display: flex;
    flex-direction: column;
    align-items: center;
    gap: 14px;
    margin-bottom: 60px;
  }
  .brand-square {
    width: 80px;
    height: 80px;
    background: var(--brand-blue);
  }
  .brand-name--front {
    font-size: 16px;
    font-weight: 700;
    color: var(--brand-blue);
    white-space: nowrap;
  }
  .contact {
    display: flex;
    flex-direction: column;
    width: 220px;
  }
  .person-name {
    font-size: 21px;
    font-weight: 700;
    color: var(--brand-blue);
    line-height: 1.1;
  }
  .person-title {
    font-size: 14px;
    color: var(--ink-soft);
    margin-bottom: 16px;
  }
  .contact-line {
    display: flex;
    align-items: center;
    gap: 7px;
    font-size: 13.5px;
    color: var(--ink);
    line-height: 1.6;
    white-space: nowrap;
  }
  .contact-icon { width: 12px; height: 12px; flex: none; fill: var(--brand-blue); }
</style>
</head>
<body>
  <section class="card card--back" aria-label="Card back">
    <span class="brand-dot"></span>
    <span class="brand-name--back">Rollers &amp; Glides.com</span>
  </section>

  <section class="card card--front" aria-label="Card front">
    <div class="front-brand">
      <span class="brand-square"></span>
      <span class="brand-name--front">Rollers &amp; Glides.com</span>
    </div>
    <div class="contact">
      <p class="person-name">Marcus Tilden</p>
      <p class="person-title">President</p>
      <p class="contact-line">
        <svg class="contact-icon" viewBox="0 0 12 12" aria-hidden="true"><path d="M2.5 1h2l1 2.5-1.3 1a6 6 0 0 0 2.3 2.3l1-1.3 2.5 1v2a1 1 0 0 1-1 1A9 9 0 0 1 1.5 2a1 1 0 0 1 1-1z"/></svg>
        555.214.8890
      </p>
      <p class="contact-line">
        <svg class="contact-icon" viewBox="0 0 12 12" aria-hidden="true"><path d="M1 2.5h10v7H1z M1.5 3l4.5 3.5L10.5 3" stroke="#fff" stroke-width="0.9"/></svg>
        Marcus@rollersandglides.com
      </p>
      <p class="contact-line">
        <svg class="contact-icon" viewBox="0 0 12 12" aria-hidden="true"><circle cx="6" cy="6" r="5.2"/><path d="M0.8 6h10.4M6 0.8c-2.6 3-2.6 7.4 0 10.4M6 0.8c2.6 3 2.6 7.4 0 10.4" stroke="#fff" stroke-width="0.8" fill="none"/></svg>
        www.rollersandglides.com
      </p>
    </div>
  </section>
</body>
</html>
```